Business Card Design Project - KLB

I am looking for a more sophisticated card design for my company,
"The Kestrel Bureau"

We are a consultancy focused on strategy and change in Associations and professional organisations.

I am a lawyer and psychologist with a PhD and so am looking for something that communicates seriousness and credibility but also quirky creative solutions for strategic problems, which is my field of speciality.

I am looking for something that is quietly spoken, rather than loud colours ('credible' and 'creative' are the two adjectives that I think of as competing here).

I particularly like an embossed card style - heavy white card with plain white or white and black or white and grey text.

The key logo image for the company is a question mark and I am open to suggestions and ideas on design.

I have attached a file that includes a couple of styles that have caught my eye and my thoughts on them. Hopefully they communicate what I'm looking for.
Updates

Thank you for all the great suggestions and designs.

I really appreciated the effort and creative energy you put into your designs. I have now closed the project after selecting a design and advising the successful designer of the card that I am happy with.

Regards

Target Market(s)

Organisations (CEO's and Boards), Governments, Legal professionals, Membership Associations and aspiring professionals.

Industry/Entity Type

Lawyer

Requirements
Must have
• The key logo element is a question mark (?) and this needs to be incorporated.

Embossed style - cut outs or other design ideas interest me too.

The attached file has a number of sample ideas and comments on each one that I like.
Should not have
• I like crisp, modern fonts (Myriads etc...) and do not like embellished fonts or Times etc...

```html
<!DOCTYPE html>
<html lang="en">
<head>
<meta charset="utf-8">
<title>The Kestrel Bureau — Business Card</title>
<link rel="stylesheet" href="https://fonts.googleapis.com/css2?family=PT+Sans+Narrow:wght@400;700&display=swap">
<style>
  :root {
    --page-bg: #e9eaeb;
    --card-white: #ffffff;
    --card-black: #0a0a0a;
    --card-black-glow: #3a3a3a;
    --ink: #1a1a1a;
    --ink-soft: #333333;
    --paper-text: #ffffff;
    --card-shadow: rgba(0, 0, 0, 0.18);
  }
  * { margin: 0; padding: 0; box-sizing: border-box; }
  html, body {
    width: 1200px;
    height: 900px;
    overflow: hidden;
    background: var(--page-bg);
    font-family: "PT Sans Narrow", "Arial Narrow", sans-serif;
  }
  .canvas {
    position: relative;
    width: 1200px;
    height: 900px;
  }

  /* Front of card */
  .card-front {
    position: absolute;
    left: 72px;
    top: 260px;
    width: 510px;
    height: 310px;
    display: flex;
    background: var(--card-white);
    box-shadow: 0 2px 10px var(--card-shadow);
  }
  .brand-panel {
    width: 190px;
    height: 100%;
    background: linear-gradient(180deg, var(--card-black) 0%, #202020 55%, #5a5a5a 100%);
    display: flex;
    flex-direction: column;
    align-items: center;
    justify-content: center;
    gap: 18px;
    padding: 0 14px;
  }
  .brand-mark {
    width: 62px;
    height: 62px;
    border-radius: 50%;
    background: var(--paper-text);
  }
  .brand-name {
    color: var(--paper-text);
    font-weight: 700;
    font-size: 24px;
    line-height: 1.05;
    text-align: center;
    text-transform: uppercase;
    letter-spacing: 0.5px;
  }
  .details {
    padding: 98px 0 0 26px;
    color: var(--ink);
  }
  .person-name {
    font-weight: 700;
    font-size: 21px;
    line-height: 1.1;
  }
  .person-role {
    font-size: 18px;
    line-height: 1.2;
    margin-bottom: 18px;
  }
  .contact-list {
    list-style: none;
    font-size: 15.5px;
    line-height: 1.45;
    color: var(--ink-soft);
  }
  .contact-list li {
    display: flex;
  }
  .contact-label {
    width: 30px;
    flex: none;
  }

  /* Back of card */
  .card-back {
    position: absolute;
    left: 626px;
    top: 304px;
    width: 512px;
    height: 308px;
    background: radial-gradient(ellipse 55% 70% at 50% 45%, var(--card-black-glow) 0%, #151515 60%, var(--card-black) 100%);
    box-shadow: 0 2px 10px var(--card-shadow);
    display: flex;
    flex-direction: column;
    align-items: center;
    justify-content: center;
    gap: 22px;
  }
  .card-back .brand-mark {
    width: 84px;
    height: 84px;
  }
  .card-back .brand-name {
    font-size: 34px;
  }
</style>
</head>
<body>
<main class="canvas">

  <section class="card-front" aria-label="Business card, front">
    <div class="brand-panel">
      <div class="brand-mark" aria-hidden="true"></div>
      <p class="brand-name">The Kestrel<br>Bureau</p>
    </div>
    <div class="details">
      <h1 class="person-name">Dr. Mara Ellison</h1>
      <p class="person-role">Director</p>
      <ul class="contact-list">
        <li><span class="contact-label">M ::</span><span>+61 400 215 730</span></li>
        <li><span class="contact-label">P ::</span><span>+612 9040 6218</span></li>
        <li><span class="contact-label">E ::</span><span>mara@kestrelbureau.com.au</span></li>
        <li><span class="contact-label">PO ::</span><span>P.O. Box 1184, Elmford Park<br>Sydney, Australia</span></li>
      </ul>
    </div>
  </section>

  <section class="card-back" aria-label="Business card, back">
    <div class="brand-mark" aria-hidden="true"></div>
    <p class="brand-name">The Kestrel Bureau</p>
  </section>

</main>
</body>
</html>
```